Launch Website

A very simple, but attractive website (template preferred) is required in a common format - HTML5 or Wordpress etc.
It should be easily user updateable for updates.
Pages it needs:
-Home Page with menu bar, company logo and 1 large graphic/picture and two smaller graphics/logos.
- What we do
- How we do it
- About Us
- Guarantees
- Results
- Contact Page with Enquiry Form
- Provision for a blog to be added later

Most pages will be approx 150 words text with some small/medium images.
We have our own domain & hosting.

A "less is more" design approach would be encouraged.

Target Market(s)

Vehicle Fleet Managers

Industry/Entity Type

It Company

Font styles to use
Sans Serif

Colors
9bcb3c

Requirements
Must have
• Corporate Style. No Fluff.
Nice to have
• Images of LIght Commerical vehicles and trucks

Am ok with white background throughout site.
Colours should match/complement company logo.
Should not have
• Should not be too "busy"

```html
<!DOCTYPE html>
<html lang="en">
<head>
<meta charset="utf-8">
<title>Cerulean Tune — Fleet Engine Optimisation</title>
<link href="https://fonts.googleapis.com/css2?family=Roboto+Condensed:wght@400;700&family=Roboto:wght@300;400;500&display=swap" rel="stylesheet">
<style>
  :root{
    --brand-blue:#1a9ad6;
    --band-blue:#1a4f86;
    --band-blue-dark:#123e6d;
    --ink:#3a3a3a;
    --muted:#8a8a8a;
    --rule:#d9d9d9;
    --alert-red:#d9232d;
    --footer-bg:#eeeeee;
    --button-bg:#c9c9c9;
    --callout-bg:#060606;
    --hero-top:#8fb8de;
    --hero-bottom:#c9d6e2;
    --white:#ffffff;
  }
  *{box-sizing:border-box;margin:0;padding:0}
  html,body{width:1200px;height:1003px;overflow:hidden;background:var(--white)}
  body{position:relative;font-family:"Roboto",Arial,sans-serif;color:var(--ink)}

  .site-header{position:absolute;left:0;top:0;width:1200px;height:102px;
    background:linear-gradient(#ffffff,#f1f1f1)}
  .brand{position:absolute;left:131px;top:30px;display:flex;align-items:center;gap:10px}
  .brand-dot{width:34px;height:34px;border-radius:50%;background:var(--brand-blue)}
  .brand-name{font-family:"Roboto Condensed",Arial,sans-serif;font-weight:700;font-size:30px;color:#2b2b2b}

  .contact-strip{position:absolute;right:134px;top:26px;text-align:right;font-size:14px;color:var(--muted);line-height:19px}
  .contact-strip .phone{color:var(--alert-red);font-size:20px}
  .contact-strip .email{color:var(--ink)}
  .contact-icon{position:absolute;left:808px;top:26px}

  .hero-band{position:absolute;left:0;top:102px;width:1200px;height:443px;
    background:linear-gradient(var(--band-blue),var(--band-blue-dark))}
  .main-nav{position:absolute;top:116px;left:0;width:1200px;height:20px}
  .main-nav a{position:absolute;top:0;color:var(--white);text-decoration:none;
    font-family:"Roboto",Arial,sans-serif;font-weight:500;font-size:14px;text-transform:uppercase}

  .slider{position:absolute;left:131px;top:155px;width:938px;height:467px;background:var(--white);
    box-shadow:0 22px 18px -14px rgba(0,0,0,.35)}
  .slide-image{position:absolute;left:9px;top:9px;width:920px;height:450px;
    background:linear-gradient(180deg,var(--hero-top),var(--hero-bottom))}
  .callout{position:absolute;left:546px;top:54px;width:361px;height:174px}
  .callout svg{position:absolute;left:0;top:0}
  .callout-text{position:absolute;left:64px;top:24px;font-family:"Roboto Condensed",Arial,sans-serif;color:var(--white);line-height:1}
  .callout-text .lead{font-size:23px}
  .callout-text .small{font-size:18px;color:var(--brand-blue);margin-top:8px}
  .callout-text .big{font-size:50px;font-weight:700;color:var(--brand-blue)}
  .callout-text .big span{font-size:32px}
  .callout-text .tail{font-size:23px;margin-left:6px;margin-top:6px}
  .partner-badge{position:absolute;top:355px;width:129px;height:78px;background:var(--white)}
  .partner-badge.first{left:634px}
  .partner-badge.second{left:773px}
  .slide-dots{position:absolute;left:20px;top:424px;display:flex;gap:4px}
  .slide-dots span{width:8px;height:8px;background:var(--white)}
  .slide-dots span.active{background:var(--brand-blue)}

  .features{position:absolute;left:131px;top:680px;display:flex;gap:38px}
  .feature{width:206px}
  .feature h2{font-family:"Roboto Condensed",Arial,sans-serif;font-weight:400;font-size:20px;color:var(--brand-blue);
    text-transform:uppercase;padding-bottom:8px;border-bottom:1px solid var(--rule);position:relative}
  .feature h2::after{content:"";position:absolute;left:0;bottom:-2px;width:80px;height:3px;background:var(--brand-blue)}
  .feature p{margin-top:18px;font-size:12.8px;line-height:18.6px;color:var(--muted);font-weight:300;height:84px}
  .read-more{display:inline-block;margin-top:22px;background:var(--button-bg);color:var(--white);
    font-size:11.5px;padding:5px 10px;text-decoration:none}

  .site-footer{position:absolute;left:0;top:922px;width:1200px;height:81px;background:var(--footer-bg)}
  .legal{position:absolute;left:131px;top:22px;font-size:12.5px;line-height:19px;color:var(--muted)}
  .legal a{color:var(--muted);text-decoration:none}
  .social{position:absolute;left:960px;top:26px;display:flex;gap:8px}
  .social a{width:30px;height:30px;background:var(--band-blue)}
</style>
</head>
<body>
  <header class="site-header">
    <div class="brand"><span class="brand-dot"></span><span class="brand-name">Cerulean Tune</span></div>
    <svg class="contact-icon" width="40" height="52" viewBox="0 0 40 52" aria-hidden="true">
      <path d="M10 4 C4 8 2 20 6 32 C10 42 18 48 26 46" fill="none" stroke="#2b2b2b" stroke-width="4" stroke-linecap="round"/>
      <path d="M22 44 C30 46 36 48 38 50" fill="none" stroke="#2b2b2b" stroke-width="1.5"/>
    </svg>
    <div class="contact-strip">
      <div>Contact us on <span class="phone">(02)5550 1472</span></div>
      <div>or email us <span class="email">info@ceruleantune.com</span></div>
    </div>
  </header>

  <div class="hero-band"></div>

  <nav class="main-nav">
    <a href="#" style="left:168px">Home</a>
    <a href="#" style="left:256px">What we do</a>
    <a href="#" style="left:390px">How we do it</a>
    <a href="#" style="left:530px">About us</a>
    <a href="#" style="left:643px">Guarantees</a>
    <a href="#" style="left:778px">Results</a>
    <a href="#" style="left:882px">Contact</a>
    <a href="#" style="left:991px">Blog</a>
  </nav>

  <section class="slider">
    <div class="slide-image" role="img" aria-label="Photo of a white semi-trailer truck on the road">
      <div class="callout">
        <svg width="361" height="174" viewBox="0 0 361 174" aria-hidden="true">
          <polygon points="0,0 361,0 361,174 30,174" fill="#1a9ad6"/>
          <polygon points="8,0 361,0 361,166 38,166" fill="#060606"/>
        </svg>
        <div class="callout-text">
          <div class="lead">We help diesel vehicle fleets</div>
          <div class="small">save up to</div>
          <div class="big">20% <span>FUEL COSTS</span></div>
          <div class="tail">by optimising their engines.</div>
        </div>
      </div>
      <div class="partner-badge first" role="img" aria-label="Industry association membership badge"></div>
      <div class="partner-badge second" role="img" aria-label="Partner badge"></div>
      <div class="slide-dots"><span class="active"></span><span></span><span></span></div>
    </div>
  </section>

  <main class="features">
    <article class="feature">
      <h2>About us</h2>
      <p>Keystone Fleet have combined over 50 years experience in all aspects of the automotive industry including commercial fleet and diesel engines. We are the ...</p>
      <a class="read-more" href="#">Read More</a>
    </article>
    <article class="feature">
      <h2>What we do</h2>
      <p>Keystone Fleet delivers award winning, ISO 9001 certified diesel engine ECU remapping for fleet operations. As Principal Australian Fleet Agent for Cerulean Tune...</p>
      <a class="read-more" href="#">Read More</a>
    </article>
    <article class="feature">
      <h2>How we do it</h2>
      <p>Keystone Fleet will conduct an obligation Free Consultation with your Fleet Representatives to determine your Fleets needs, and identify any customization...</p>
      <a class="read-more" href="#">Read More</a>
    </article>
    <article class="feature">
      <h2>Why</h2>
      <p>We've acted on customer requests for cost effective, financially attractive solutions to reduce fuel and operating costs whilst also reducing environmental foot...</p>
      <a class="read-more" href="#">Read More</a>
    </article>
  </main>

  <footer class="site-footer">
    <div class="legal">
      <div>Copyright 2014 Cerulean Tune. All Rights Reserved.</div>
      <div><a href="#">Privacy Policy</a> | <a href="#">Terms and Conditions</a></div>
    </div>
    <div class="social">
      <a href="#" aria-label="Social profile one"></a>
      <a href="#" aria-label="Social profile two"></a>
      <a href="#" aria-label="Social profile three"></a>
    </div>
  </footer>
</body>
</html>
```